Innovative Strategic IT Solutions and Management Consulting

Looking for a fresh design idea to represent a company which specializes in innovative strategic IT solutions focusing on information assurance, enterprise content management, health information technology, web applications, strategic IT solutions and solutions architect.

KELTO...the company name means "new beginning" in Greek or the acronym for Keep-Every-Layer-Tightly-Organized. We pride ourselves in understanding the client's business and needs before proposing an innovative solutions.

Innovation / Secure / Strategy - the core motto

Color: Maroon / Burgundy / Silver / White / Grey / Black

Primary focus color: Burgundy / Silver

```html
<!DOCTYPE html>
<html lang="en">
<head>
<meta charset="utf-8">
<title>KELTO – Innovative Strategic IT Solutions</title>
<link href="https://fonts.googleapis.com/css2?family=Arimo:wght@400;700&display=swap" rel="stylesheet">
<style>
:root{
  --blue:#1c5ff2;
  --blue-dark:#0d3fc4;
  --maroon:#9c0b0b;
  --red:#d81e1e;
  --band-dark:#3d3d3d;
  --band-light:#e6e6e6;
  --footer:#3b3b3b;
  --footer-bottom:#111;
  --ink:#222;
  --muted:#555;
  --silver:#c8c8c8;
  --white:#fff;
}
*{box-sizing:border-box;margin:0;padding:0}
html,body{width:960px;height:1200px;overflow:hidden}
body{position:relative;font-family:"Arimo",Arial,sans-serif;color:var(--ink);background:var(--white);font-size:10px}
.abs{position:absolute}
.top-strip{left:0;top:0;width:960px;height:13px;background:var(--band-dark)}
.header{left:0;top:13px;width:960px;height:105px;background:var(--white)}
.brand{left:130px;top:52px;display:flex;align-items:center;gap:10px}
.brand-dot{width:30px;height:30px;border-radius:50%;background:var(--maroon)}
.brand-name{font-size:30px;font-weight:700;color:var(--maroon);letter-spacing:1px}
.phone{left:436px;top:60px;display:flex;align-items:center;gap:6px;font-size:22px;font-weight:700;color:#333}
.search{left:625px;top:64px;display:flex;gap:5px}
.search-field{width:146px;height:19px;border:1px solid #bbb;background:#fff}
.search-btn{width:50px;height:19px;background:var(--maroon);color:#fff;font-size:10px;text-align:center;line-height:19px}
.nav{left:0;top:118px;width:960px;height:32px;background:linear-gradient(#3a7bff,var(--blue) 55%,var(--blue-dark))}
.nav-item{top:0;height:32px;line-height:32px;text-align:center;color:#fff;font-size:12px;border-left:1px solid rgba(255,255,255,.35)}
.band-dark{left:0;top:150px;width:960px;height:323px;background:var(--band-dark)}
.band-light{left:0;top:473px;width:960px;height:227px;background:var(--band-light)}
.slider{left:130px;top:166px;width:700px;height:260px;background:linear-gradient(#f4f4f4,#dcdcdc);border-radius:4px;box-shadow:0 6px 10px rgba(0,0,0,.35)}
.slide-photo{left:143px;top:180px;width:673px;height:238px;background:linear-gradient(110deg,#1e1e24 0%,#4a4f5c 35%,#9fb2c9 60%,#dfe6ee 100%);border-radius:2px}
.slide-caption{left:143px;top:345px;width:673px;text-align:center;font-size:38px;color:#fff;text-shadow:0 2px 4px rgba(0,0,0,.5)}
.dots{left:460px;top:402px;display:flex;gap:4px}
.dots span{width:6px;height:6px;background:#fff}
.dots span.on{background:var(--red)}
.arrow{top:285px;width:30px;height:30px;border-radius:50%;background:#eee;border:2px solid #999}
.card{top:452px;width:212px;height:226px;background:linear-gradient(#fff,#ececec);border-radius:4px;box-shadow:0 3px 6px rgba(0,0,0,.25)}
.card-head{position:absolute;left:0;top:0;width:212px;height:60px}
.card-title{position:absolute;left:0;top:10px;width:212px;text-align:center;color:#fff;font-size:19px;font-weight:700}
.card-photo{position:absolute;left:8px;top:52px;width:196px;height:80px}
.card-text{position:absolute;left:12px;top:140px;width:190px;font-size:9.5px;line-height:1.3;color:#222}
.card-list{position:absolute;left:12px;top:138px;list-style:none;font-size:9.5px;line-height:1.35}
.card-list li{display:flex;align-items:center;gap:5px}
.card-btn{position:absolute;right:-4px;top:184px;width:88px;height:24px;background:var(--maroon);color:#fff;font-size:10px;text-align:center;line-height:24px}
.welcome-title{left:137px;top:718px;font-size:15px;color:#111}
.welcome-title em{font-style:normal;color:var(--red)}
.welcome-text{left:137px;width:278px;font-size:10px;line-height:1.3;color:#333;text-indent:24px}
.laptop{left:432px;top:765px;width:140px;height:115px;background:linear-gradient(135deg,#e9eef5,#3d6fb8 55%,#9aa3ad);border-radius:6px}
.btn-blue{left:505px;top:955px;width:63px;height:20px;background:var(--blue);color:#fff;border-radius:3px;font-size:10px;text-align:center;line-height:20px}
.news{left:618px;top:718px;width:207px;height:258px;background:#f6f6f6;border:1px solid #d4d4d4;border-radius:3px}
.news-head{height:24px;background:linear-gradient(#eee,#d4d4d4);padding-left:12px;line-height:24px;font-size:10px;color:#333;position:relative}
.news-toggle{position:absolute;right:10px;top:6px;width:16px;height:13px;background:#555;border-radius:2px}
.news-item{display:flex;gap:8px;padding:10px 10px 0 12px;height:65px;border-bottom:1px solid #ddd}
.news-thumb{width:48px;height:44px;border:2px solid #fff;box-shadow:0 0 2px #999;flex:none}
.news-body{font-size:8px;line-height:1.3;color:#444}
.news-body b{font-size:8.5px;color:#111}
.news-all{position:absolute;right:10px;bottom:8px;font-size:9px;color:var(--red)}
.footer{left:0;top:995px;width:960px;height:180px;background:var(--footer)}
.footer-bottom{left:0;top:1175px;width:960px;height:25px;background:var(--footer-bottom);color:#fff;font-size:10px;text-align:center;line-height:25px}
.f-head{font-size:11px;font-weight:700;color:#fff}
.f-list{list-style:none;color:#ddd;font-size:9.5px;line-height:1.2}
.contact-box{left:410px;top:1032px;width:150px;height:110px;border:1px solid #666;padding:10px;color:#ddd;font-size:9px;line-height:1.25}
.socials{left:271px;top:1116px;display:flex;gap:3px}
.socials span{width:15px;height:15px;border-radius:2px}
.news-copy{left:617px;top:1031px;width:215px;color:#ddd;font-size:9.5px;line-height:1.3}
.email-field{left:620px;top:1080px;width:136px;height:20px;background:#fff;font-size:10px;color:#333;padding-left:5px;line-height:20px}
.submit{left:762px;top:1080px;width:66px;height:21px;background:var(--blue);color:#fff;font-size:12px;text-align:center;line-height:21px}
.agree{left:622px;top:1118px;display:flex;gap:12px;color:#ddd;font-size:9.5px;line-height:1.25}
.agree i{width:12px;height:12px;background:#ddd;flex:none;margin-top:1px}
</style>
</head>
<body>
<div class="abs top-strip"></div>
<header class="abs header"></header>
<div class="abs brand"><span class="brand-dot"></span><span class="brand-name">KELTO</span></div>
<div class="abs phone">
  <svg width="16" height="22" viewBox="0 0 16 22"><path d="M4 1l3 4-2 3c1 3 2 6 5 8l2-2 3 3-3 4C6 20 1 12 2 4z" fill="var(--maroon)"/></svg>
  (200) 555 0148
</div>
<div class="abs search"><div class="search-field"></div><div class="search-btn">Search</div></div>

<nav class="abs nav">
  <div class="abs nav-item" style="left:130px;width:89px">Home</div>
  <div class="abs nav-item" style="left:219px;width:104px">About Us</div>
  <div class="abs nav-item" style="left:323px;width:101px">Services</div>
  <div class="abs nav-item" style="left:424px;width:100px">Products</div>
  <div class="abs nav-item" style="left:524px;width:110px">Contact Us</div>
  <div class="abs nav-item" style="left:634px;width:92px">Blog</div>
  <div class="abs nav-item" style="left:726px;width:104px;border-right:1px solid rgba(255,255,255,.35)">Login</div>
</nav>

<div class="abs band-dark"></div>
<div class="abs band-light"></div>

<section class="abs slider"></section>
<div class="abs slide-photo" role="img" aria-label="Photo of a businessman working on a laptop in a bright office"></div>
<div class="abs slide-caption">Innovation, Secure, Strategy</div>
<div class="abs dots"><span class="on"></span><span></span><span></span><span></span></div>
<svg class="abs arrow" style="left:118px" viewBox="0 0 30 30"><path d="M18 8l-7 7 7 7" stroke="#333" stroke-width="3" fill="none"/></svg>
<svg class="abs arrow" style="left:811px" viewBox="0 0 30 30"><path d="M12 8l7 7-7 7" stroke="#333" stroke-width="3" fill="none"/></svg>

<article class="abs card" style="left:150px">
  <svg class="card-head" viewBox="0 0 212 60"><defs><linearGradient id="cg" x1="0" y1="0" x2="0" y2="1"><stop offset="0" stop-color="#3a7bff"/><stop offset="1" stop-color="#0d3fc4"/></linearGradient></defs><path d="M0 4a4 4 0 0 1 4-4h204a4 4 0 0 1 4 4v44Q106 30 0 48z" fill="url(#cg)"/></svg>
  <div class="card-title">Who We Are</div>
  <div class="card-photo" role="img" aria-label="Photo of a smiling business team" style="background:linear-gradient(90deg,#3b3f4a,#c9b8a8 50%,#2e323c)"></div>
  <p class="card-text">Lorem ipsum dolor sit amet, consecteteur adipiscing elit. sed diem nonumy inconvalis gravida neque...</p>
  <div class="card-btn">Read more</div>
</article>
<article class="abs card" style="left:374px">
  <svg class="card-head" viewBox="0 0 212 60"><path d="M0 4a4 4 0 0 1 4-4h204a4 4 0 0 1 4 4v44Q106 30 0 48z" fill="url(#cg)"/></svg>
  <div class="card-title">Contact Us</div>
  <div class="card-photo" role="img" aria-label="Photo of hands typing on a keyboard" style="background:linear-gradient(120deg,#d8d8d8,#4a4a4a 55%,#9a9a9a)"></div>
  <p class="card-text">Lorem ipsum dolor sit amet, consecteteur adipiscing elit. sed diem nonumy inconvalis gravida neque...</p>
  <div class="card-btn">Read more</div>
</article>
<article class="abs card" style="left:600px">
  <svg class="card-head" viewBox="0 0 212 60"><path d="M0 4a4 4 0 0 1 4-4h204a4 4 0 0 1 4 4v44Q106 30 0 48z" fill="url(#cg)"/></svg>
  <div class="card-title">Services</div>
  <div class="card-photo" role="img" aria-label="Photo of a hand touching a digital technology interface" style="background:linear-gradient(120deg,#1d3a66,#8fb2d8 50%,#2a4d7c)"></div>
  <ul class="card-list">
    <li><svg width="9" height="9" viewBox="0 0 9 9"><path d="M1 5l2 3 5-7" stroke="var(--blue)" stroke-width="2" fill="none"/></svg>Information Assurance</li>
    <li><svg width="9" height="9" viewBox="0 0 9 9"><path d="M1 5l2 3 5-7" stroke="var(--blue)" stroke-width="2" fill="none"/></svg>Enterprise Information Management</li>
    <li><svg width="9" height="9" viewBox="0 0 9 9"><path d="M1 5l2 3 5-7" stroke="var(--blue)" stroke-width="2" fill="none"/></svg>Health Information Technology</li>
    <li><svg width="9" height="9" viewBox="0 0 9 9"><path d="M1 5l2 3 5-7" stroke="var(--blue)" stroke-width="2" fill="none"/></svg>Web applications...</li>
  </ul>
  <div class="card-btn">Read more</div>
</article>

<h1 class="abs welcome-title" style="font-weight:400">Welcome to <em>KELTO (Keep Every Layer Tightly Organized)</em></h1>
<p class="abs welcome-text" style="top:748px">Lorem ipsum dolor sit amet, consectetuer adipiscing elit. set diem nonumy in convalis gravida neque. Nulla gravida vestibulum metis a acumsan, aliquam in sagittis ut. Solicitudin sed massa ud enim veniam. Curabitur tempus sem vitae mi vestibulum volutpat malesu ada arat vestibulum. Sed aliquam dolor at dolor conse quat gravida. Fusce mineque tempus nec fequat sit amet. Tincidunt ut leo. Nam semper omare enim.</p>
<p class="abs welcome-text" style="top:843px">Lorem ipsum dolor sit amet, consectetuer adipiscing elit. set diem nonumy inconvalis gravida neque. Nulla gravida vestibulum metis a acumsan, aliquam in sagittis ut. Solicitudin sed massa ud enim veniam. Curabitur tempus sem vitae mi vestibulum volutpat malesu ada arat vestibulum. sed aliaiilwuam dolor at dolor conse quat gravida. Fusce mineque tempus neq fequat sit amet. Tinci dunt ut leo. Nam semper omare enim.</p>
<div class="abs laptop" role="img" aria-label="Illustration of a laptop with rising bar charts and a pie chart"></div>
<div class="abs btn-blue">read more</div>

<aside class="abs news">
  <div class="news-head">LATEST NEWS<span class="news-toggle"></span></div>
  <div class="news-item"><div class="news-thumb" role="img" aria-label="Photo of a businesswoman" style="background:linear-gradient(#6b7a8c,#c7a68a)"></div><div class="news-body"><b>Lorem Ipsum dolor sit amet</b><br>January, 15th 2014<br>Lorem ipsum dolor sit amet,conse ctteteur adipiscing elit. set</div></div>
  <div class="news-item"><div class="news-thumb" role="img" aria-label="Photo of tablet devices" style="background:linear-gradient(#5b8fd0,#dfe9f5)"></div><div class="news-body"><b>Lorem Ipsum dolor sit amet</b><br>February 17th 2014<br>Lorem ipsum dolor sit amet,conse ctteteur adipiscing elit. set</div></div>
  <div class="news-item" style="border:none"><div class="news-thumb" role="img" aria-label="Photo of a digital network concept" style="background:linear-gradient(#2a4a7a,#a5c2e2)"></div><div class="news-body"><b>Lorem Ipsum dolor sit amet</b><br>March, 22th 2014<br>Lorem ipsum dolor sit amet,conse ctteteur adipiscing elit. set</div></div>
  <div class="news-all">View All</div>
</aside>

<footer class="abs footer"></footer>
<div class="abs f-head" style="left:163px;top:1007px">Main menu</div>
<ul class="abs f-list" style="left:163px;top:1031px"><li>Home</li><li>About us</li><li>Services</li><li>Products</li><li>Blog</li><li>Contact Us</li><li>Login</li><li>Testimonials</li><li>Latest News</li></ul>
<div class="abs f-head" style="left:271px;top:1007px">Usefull Links</div>
<ul class="abs f-list" style="left:271px;top:1031px"><li>Sitemap</li><li>Terms &amp; Conditions</li><li>Privacy Policy</li><li>Help</li><li>FAQ's</li></ul>
<div class="abs f-list" style="left:271px;top:1100px">Follow Us on &nbsp;:</div>
<div class="abs socials"><span style="background:#3aa0e0"></span><span style="background:#3b5b9a"></span><span style="background:#f08a1c"></span><span style="background:#1a7ab8"></span></div>
<div class="abs f-head" style="left:421px;top:1007px">Get In Touch</div>
<div class="abs contact-box">Harbor Line Inc<br><br>Address :<br>lorem ipsum, 1238943,<br>your city, ZIP.<br><br>Phone : XXX - XXXX - XXX<br>Fax &nbsp;&nbsp;&nbsp;: XXX - XXXX - XXXX<br>email &nbsp;: info@KELTO.com</div>
<div class="abs f-head" style="left:617px;top:1007px">Newsletter</div>
<p class="abs news-copy">Receive our newdletter weekly.<br>We will never share your any information to the 3rd parry.</p>
<div class="abs email-field">Your email address</div>
<div class="abs submit">SUBMIT</div>
<div class="abs agree"><i></i><span>by clicking this button, you agree<br>with our terms &amp; Conditions</span></div>
<div class="abs footer-bottom">Copyright &copy; 2014, KELTO.com. All rights resreved.</div>
</body>
</html>
```